Tidewell Consulting Schedule Of Rates

We need a brochure / proposal for our new company. Our company is a start up based in Australia who provides engineering and sales support to other renewable energy companies. Our brochure is a pitch-deck / sales item that catalogues our key services. We are engineering consultants.

Our website is www.tidewellpartners.com.au. Please review the website to get a feel of colour schemes etc.

We are looking for a strong, trustworthy feel, but the brochure also needs to be sales driven and to the point.

The second page that contains the $30 price point needs to be loud and clear.

The use of relevant icons throughout the document will be viewed favorably.

Please format the tables to look attractive.

The document will need to be in an editable format so content can be edited by us at a later date.

Please feel free to use the pics within the attached word document. The winning design will be provided with updated, clearer images upon request.

Thank you

Target Market(s)

Businesses that either sell or install solar PV and other renewable energy systems in Australia. Most of target market are likely to be electrical contractors.

Industry/Entity Type

Engineering

Colors
0255a3
0492cd
ffffff

Requirements
Must have
• Icons, graphics presentation, Clean and Clear, Business oriented. Sharp sales feel
Nice to have
• solar picture backgrounds maybe
Should not have
• cartoons, over sales driven,

```html
<!DOCTYPE html>
<html lang="en">
<head>
<meta charset="utf-8">
<title>Tidewell Consulting – Design &amp; Support Services Schedule Of Rates</title>
<link rel="stylesheet" href="https://fonts.googleapis.com/css2?family=Exo+2:wght@300;400;700&display=swap">
<style>
  :root {
    --ink: #0b0b0c;
    --panel-black: #050506;
    --panel-grey: #7c7d80;
    --sliver-grey: #8e8f92;
    --paper: #ffffff;
    --paper-shade: #d9d9db;
    --text-light: #ffffff;
    --text-soft: #e6e6e8;
    --solar-deep: #0a2f6b;
    --solar-mid: #2f5fa8;
    --solar-light: #7fa3d4;
    --sun: #e8e64a;
  }
  * { margin: 0; padding: 0; box-sizing: border-box; }
  html, body { width: 848px; height: 1200px; overflow: hidden; background: var(--paper); }
  .cover {
    position: relative;
    width: 848px;
    height: 1200px;
    overflow: hidden;
    font-family: "Exo 2", "Trebuchet MS", sans-serif;
  }
  .cover-shapes { position: absolute; inset: 0; display: block; }
  .cover-title {
    position: absolute;
    left: 47px;
    top: 722px;
    color: var(--text-light);
    font-weight: 300;
    font-size: 39px;
    line-height: 56px;
    letter-spacing: 0.3px;
  }
  .cover-subtitle {
    position: absolute;
    left: 48px;
    top: 834px;
    color: var(--text-soft);
    font-weight: 300;
    font-size: 23px;
    letter-spacing: 0.4px;
  }
  .contact-list {
    position: absolute;
    left: 47px;
    top: 1071px;
    list-style: none;
    color: var(--text-light);
    font-weight: 300;
    font-size: 15px;
    line-height: 20px;
  }
  .brand-name {
    position: absolute;
    right: 26px;
    top: 1068px;
    width: 300px;
    text-align: right;
    color: var(--ink);
    font-weight: 700;
    font-size: 36px;
    line-height: 40px;
    letter-spacing: -0.5px;
  }
</style>
</head>
<body>
<main class="cover">
  <svg class="cover-shapes" width="848" height="1200" viewBox="0 0 1000 1415" xmlns="http://www.w3.org/2000/svg">
    <defs>
      <linearGradient id="solarField" x1="0" y1="0" x2="0.35" y2="1">
        <stop offset="0" stop-color="var(--solar-light)"/>
        <stop offset="0.35" stop-color="var(--solar-mid)"/>
        <stop offset="1" stop-color="var(--solar-deep)"/>
      </linearGradient>
      <radialGradient id="sunGlow" cx="0.72" cy="0.02" r="0.5">
        <stop offset="0" stop-color="var(--sun)" stop-opacity="0.95"/>
        <stop offset="0.5" stop-color="var(--sun)" stop-opacity="0.25"/>
        <stop offset="1" stop-color="var(--sun)" stop-opacity="0"/>
      </radialGradient>
      <linearGradient id="paperShade" x1="1" y1="0" x2="0.3" y2="1">
        <stop offset="0" stop-color="var(--paper-shade)"/>
        <stop offset="1" stop-color="var(--paper)"/>
      </linearGradient>
    </defs>
    <g role="img" aria-label="Photograph of rows of blue solar panels in a field under bright sunlight">
      <rect x="0" y="0" width="1000" height="1080" fill="url(#solarField)"/>
      <rect x="0" y="0" width="1000" height="1080" fill="url(#sunGlow)"/>
    </g>
    <polygon class="panel-title" points="0,780 722,780 578,1078 0,1078" fill="var(--panel-black)"/>
    <polygon class="accent-sliver" points="730,780 768,780 728,862 690,862" fill="var(--sliver-grey)"/>
    <polygon class="panel-contact" points="0,1075 574,1075 405,1415 0,1415" fill="var(--panel-grey)"/>
    <polygon class="panel-brand" points="600,1075 1000,1075 1000,1415 432,1415" fill="url(#paperShade)"/>
    <polygon class="divider-stripe" points="574,1075 600,1075 432,1415 405,1415" fill="var(--panel-black)"/>
  </svg>

  <h1 class="cover-title">Design &amp; Support Services<br>Schedule Of Rates</h1>
  <p class="cover-subtitle">Grid and Off Grid 5kW – 10MW</p>

  <ul class="contact-list">
    <li>P: 03 9147 2260 | M: 0412 308 671</li>
    <li>E: sales@tidewellpartners.com.au</li>
    <li>W: www.tidewellpartners.com.au</li>
  </ul>

  <p class="brand-name">Tidewell Consulting</p>
</main>
</body>
</html>
```